OLU58 biz card & Stationery

LU58 is a personalized shopping experience brought to you, that lets you find and discover fashion goods through a collection of boutiques curated by taste-makers - celebrities, stylists, designers, and fashion bloggers. Boutiques uses visual technology to help fashionistas discover and shop their look and creates the opportunity for designers to showcase their collections and latest inspirations online.

OLU58 is built on technology developed by our team of fashion experts who work with engineers to “teach” our computer systems to understand various patterns, pairings, and genre definitions. When signed into your account, OLU58 learns about your style and preferences and in turn, provides you better results and recommendations over time. Ultimately, OLU58 will provide shoppers with a much richer and interactive shopping experience and help drive traffic to retailers' websites.

We need a definitely cool business card. The card must be black! And must use our official logo which can be download from OLU58.com

The address for Letter head and evenlop, please use 4872 Crestwick Parkway, Sutie 510 Los Angeles CA90412, email will be anyone@OLU58.com, website is www.OLU58.com

thanks

We received some of the design, thanks. But most of the design are not what we want. We need a very clean version with black ground, you may also use some dark gray to add the element. please take a look at http://morvalstudio.no/work/#pelter__ostrama/, we do like this kind of design very much. hope it help.

```html
<!DOCTYPE html>
<html lang="en">
<head>
<meta charset="utf-8">
<title>OLU58 — Business Card &amp; Stationery</title>
<link rel="stylesheet" href="https://fonts.googleapis.com/css2?family=Josefin+Sans:wght@400;700&display=swap">
<style>
  :root {
    --ink: #141414;
    --band: #1e1e1e;
    --paper: #ffffff;
    --tag-grey: #b4b4b4;
    --decor-grey: #bdbdbd;
    --light-text: #f2f2f2;
    --bg-top: #f0f0f0;
    --bg-mid: #9c9c9c;
    --bg-low: #c4c4c4;
    --brand-font: "Josefin Sans", "Helvetica Neue", sans-serif;
  }
  * { box-sizing: border-box; margin: 0; padding: 0; }
  html, body { width: 1200px; height: 1200px; overflow: hidden; }
  body {
    position: relative;
    background: linear-gradient(180deg, var(--bg-top) 0%, #d8d8d8 30%, var(--bg-mid) 62%, var(--bg-low) 100%);
  }
  .item { position: absolute; overflow: hidden; box-shadow: 6px 8px 14px rgba(0,0,0,.45); }
  .item > svg { display: block; width: 100%; height: 100%; }

  .wordmark { font-family: var(--brand-font); font-weight: 700; fill: var(--paper); }
  .card .wordmark { fill: var(--light-text); }
  .tagline { font-family: var(--brand-font); font-weight: 400; fill: var(--tag-grey); }
  .details { font-family: var(--brand-font); font-weight: 400; font-size: 15px; fill: var(--light-text); letter-spacing: .04em; }
  .address { font-family: var(--brand-font); font-weight: 400; font-size: 13px; fill: var(--ink); letter-spacing: .08em; }
  .decor { font-family: var(--brand-font); font-weight: 700; fill: var(--decor-grey); }

  .letterhead--front { left: 17px; top: 17px; width: 769px; height: 1100px; background: var(--paper); }
  .letterhead--back  { left: 790px; top: 70px; width: 378px; height: 1058px; background: var(--paper); }
  .envelope-back  { left: 524px; top: 596px; width: 664px; height: 406px; background: var(--paper); }
  .envelope-front { left: 524px; top: 763px; width: 542px; height: 365px; background: var(--paper); box-shadow: 4px 6px 10px rgba(0,0,0,.35); }
  .footer-band    { left: 106px; top: 1088px; width: 960px; height: 100px; background: var(--band); }

  .card--black { left: 54px; top: 372px; width: 238px; height: 412px; background: #000; }
  .card--brushed { left: 294px; top: 556px; width: 228px; height: 414px;
    background:
      repeating-linear-gradient(180deg, rgba(255,255,255,.05) 0 1px, rgba(0,0,0,.06) 1px 3px),
      radial-gradient(ellipse at 40% 55%, #6a6a6a 0%, #3a3a3a 45%, #111 100%);
  }
  .card--front { left: 106px; top: 766px; width: 238px; height: 416px;
    background:
      repeating-linear-gradient(180deg, rgba(255,255,255,.05) 0 1px, rgba(0,0,0,.07) 1px 3px),
      linear-gradient(180deg, #222 0%, #5c5c5c 30%, #2a2a2a 55%, #3a3a3a 80%, #1a1a1a 100%);
  }
</style>
</head>
<body>

  <section class="item letterhead--front" aria-label="Letterhead">
    <svg viewBox="0 0 769 1100">
      <rect width="769" height="139" fill="var(--band)"/>
      <text class="wordmark" x="397" y="139" font-size="138" textLength="372" lengthAdjust="spacingAndGlyphs">OLU58</text>
      <text class="tagline" x="313" y="175" font-size="35" textLength="456" lengthAdjust="spacingAndGlyphs">CURATED STYLE NETWORK</text>
    </svg>
  </section>

  <section class="item letterhead--back" aria-label="Letterhead second sheet">
    <svg viewBox="0 0 378 1058">
      <rect width="378" height="134" fill="var(--band)"/>
      <text class="wordmark" x="6" y="134" font-size="134" textLength="372" lengthAdjust="spacingAndGlyphs">OLU58</text>
      <text class="tagline" x="-78" y="170" font-size="35" textLength="456" lengthAdjust="spacingAndGlyphs">CURATED STYLE NETWORK</text>
    </svg>
  </section>

  <section class="item envelope-back" aria-label="Envelope back">
    <svg viewBox="0 0 664 406">
      <path d="M0 0 H664 V6 C652 72 634 114 592 132 H0 Z" fill="var(--band)"/>
      <text class="wordmark" x="120" y="130" font-size="102" textLength="280" lengthAdjust="spacingAndGlyphs">OLU58</text>
    </svg>
  </section>

  <section class="item envelope-front" aria-label="Envelope front">
    <svg viewBox="0 0 542 365">
      <text class="address" text-anchor="end" x="530" y="251">4872 CRESTWICK PARKWAY</text>
      <text class="address" text-anchor="end" x="530" y="270">SUTIE 510 LOS ANGELES CA90412</text>
      <text class="address" text-anchor="end" x="530" y="289">ANYONE@OLU58.COM</text>
      <text class="address" text-anchor="end" x="530" y="308">WWW.OLU58.COM</text>
    </svg>
  </section>

  <section class="item footer-band" aria-label="Continuation sheet footer">
    <svg viewBox="0 0 960 100">
      <text class="tagline" x="356" y="82" font-size="34" textLength="296" lengthAdjust="spacingAndGlyphs">CURATED STYLE NETWORK</text>
      <text class="wordmark" x="674" y="96" font-size="116" textLength="284" lengthAdjust="spacingAndGlyphs">OLU58</text>
    </svg>
  </section>

  <section class="item card card--black" aria-label="Business card, black">
    <svg viewBox="0 0 238 412">
      <text class="wordmark" x="48" y="90" font-size="56" textLength="188" lengthAdjust="spacingAndGlyphs">OLU58</text>
      <text class="tagline" x="28" y="114" font-size="19" textLength="208" lengthAdjust="spacingAndGlyphs">CURATED STYLE NETWORK</text>
      <g transform="translate(222 134) rotate(90)">
        <text class="details" x="0" y="0">4872 Crestwick Parkway,</text>
        <text class="details" x="0" y="22">Sutie 510 Los Angeles CA90412.</text>
        <text class="details" x="0" y="44">anyone@OLU58.com</text>
        <text class="details" x="0" y="66">www.OLU58.com</text>
      </g>
    </svg>
  </section>

  <section class="item card card--brushed" aria-label="Business card, brushed grey">
    <svg viewBox="0 0 228 414">
      <text class="wordmark" x="38" y="92" font-size="56" textLength="188" lengthAdjust="spacingAndGlyphs">OLU58</text>
      <text class="tagline" x="18" y="114" font-size="19" textLength="208" lengthAdjust="spacingAndGlyphs">CURATED STYLE NETWORK</text>
      <g transform="translate(180 132) rotate(90)">
        <text class="details" x="0" y="0">4872 Crestwick Parkway,</text>
        <text class="details" x="0" y="22">Sutie 510 Los Angeles CA90412.</text>
        <text class="details" x="0" y="44">anyone@OLU58.com</text>
        <text class="details" x="0" y="66">www.OLU58.com</text>
      </g>
    </svg>
  </section>

  <section class="item card card--front" aria-label="Business card, front">
    <svg viewBox="0 0 238 416">
      <text class="wordmark" x="48" y="90" font-size="56" textLength="188" lengthAdjust="spacingAndGlyphs">OLU58</text>
      <text class="tagline" x="28" y="112" font-size="19" textLength="208" lengthAdjust="spacingAndGlyphs">CURATED STYLE NETWORK</text>
      <text class="decor" x="40" y="340" font-size="84" textLength="192" lengthAdjust="spacingAndGlyphs" aria-hidden="true">OLU58</text>
      <text class="wordmark" x="74" y="400" font-size="28" textLength="96" lengthAdjust="spacingAndGlyphs">OLU58</text>
    </svg>
  </section>

</body>
</html>
```